New Graphic Design Project / Email signiture and Letterhead

I would like a new SIMPLE but high end quality modern/heavy industrial design for an email Signiture and letter head that incorporates product photos or illustrations of our products to show our customers our range of products and also show our head office in Perth Western Australia and also our Australian and international reseller locations.
in my present email signature you would see that I have other company logos these companies are old partners of ours but some are no longer so I would like to have the option to add and change them if things change in the future.
for ideas Our main products are as follows
Composite Hose
Convoluted hose
Metal expansion joints
Fabric expansion joints
Rubber Expansion joints
Please see our website for ideas and our product photos.
www.dravoline.com.au
if you need any further information please let me know
i have attached our old email signiture for reference.
Mark

Target Market(s)

Oil and Gas / Mining / Petroleum and Chemical Refineries, high end engineering

Requirements
Must have
• pictures / photos of our core products and our company capabilities to show our existing and new customers what we can do.
in the email signature - links to company face book and LinkedIn, our website
I would like to have spaces for my company partners logos and need the final file to be in a format for me to change and update all details
All so our Font is Conthrax SB
Nice to have
• the email signature, I would like this to have all the required information ( as per attached present email signature ) but also be informative / marketing to show customers what we do if possible.
the letter head can be based from the same but simple with or without product photos

```html
<!DOCTYPE html>
<html lang="en">
<head>
<meta charset="utf-8">
<title>Dravoline – Email Signature Options</title>
<link href="https://fonts.googleapis.com/css2?family=Montserrat:wght@400;500;600;700&display=swap" rel="stylesheet">
<style>
  :root {
    --ink: #1d2748;
    --grey: #4a4a4c;
    --rule: #c9c9c9;
    --gold: #f2c200;
    --white: #ffffff;
    --strip: rgba(40, 36, 34, 0.72);
  }
  * { margin: 0; padding: 0; box-sizing: border-box; }
  html, body { width: 849px; height: 1200px; overflow: hidden; background: var(--white); }
  body { position: relative; font-family: "Montserrat", Arial, sans-serif; color: var(--ink); }

  .signature {
    position: absolute; left: 153px; width: 556px; height: 370px;
    border: 0.6px solid var(--rule); background: var(--white); overflow: hidden;
  }
  .signature--sunset { top: 34px; }
  .signature--dusk { top: 422px; }
  .signature--night { top: 810px; }

  .sign-off { position: absolute; left: 34px; font-size: 7.6px; letter-spacing: 0.3px; }
  .sign-off__name { display: block; margin-top: 15px; font-size: 8.6px; letter-spacing: 0.4px; font-weight: 500; }
  .sign-off__role { display: block; font-size: 5.8px; letter-spacing: 0.3px; }

  .brand { position: absolute; left: 34px; display: flex; align-items: center; gap: 9px; }
  .brand__mark { width: 34px; height: 34px; border-radius: 50%; border: 3.5px solid var(--grey); }
  .brand__name { font-size: 19px; font-weight: 700; color: var(--grey); letter-spacing: 0.6px; }

  .office { position: absolute; left: 250px; font-size: 6px; color: var(--grey); line-height: 1.45; }
  .office__label { font-weight: 600; color: #2a2a2a; }
  .office__block + .office__block { margin-top: 9px; }

  .contact { position: absolute; left: 424px; font-size: 6px; color: var(--grey); line-height: 1.75; }
  .contact__key { font-weight: 600; color: #2a2a2a; display: inline-block; width: 11px; }
  .contact__social { display: flex; align-items: center; gap: 5px; margin-top: 2px; }
  .contact__dot { width: 8px; height: 8px; border-radius: 50%; background: #3b67b0; }

  .banner { position: absolute; left: 0; width: 100%; }
  .banner--sunset { background: linear-gradient(100deg, #5d6a5a 0%, #b98a3a 30%, #e0a64a 55%, #c98436 75%, #6f5a3a 100%); }
  .banner--dusk { background: linear-gradient(180deg, #9e6a70 0%, #b57d7c 45%, #4a4c55 70%, #23262e 100%); }
  .banner--night { background: linear-gradient(180deg, #27345e 0%, #3c4a70 40%, #8a7a4e 70%, #3a3424 100%); }

  .products {
    position: absolute; left: 0; width: 100%; display: flex; justify-content: center; align-items: center;
    font-size: 6.6px; font-weight: 600; letter-spacing: 0.8px; white-space: nowrap;
  }
  .products span + span::before { content: "|"; margin: 0 6px; }
  .products--overlay { background: var(--strip); height: 25px; }
  .products--gold { color: var(--gold); }
  .products--light { color: #f1f1f1; }
  .products--plain { color: #333; font-size: 6.2px; }
  .products--plain span + span::before { margin: 0 7px; }

  .partners { position: absolute; left: 0; top: 336px; width: 100%; display: flex; justify-content: center; align-items: center; gap: 22px; }
  .partners__badge { height: 16px; background: #b8bcc4; border-radius: 2px; }
  .partners__badge--round { width: 18px; height: 18px; border-radius: 50%; }
</style>
</head>
<body>

<!-- Option 1: sunset band, gold product line -->
<section class="signature signature--sunset">
  <p class="sign-off" style="top:101px">Thanks and Regards
    <span class="sign-off__name">MARK HALLAM</span>
    <span class="sign-off__role">Managing Director</span>
  </p>
  <div class="brand" style="top:205px"><span class="brand__mark"></span><span class="brand__name">DRAVOLINE</span></div>
  <div class="office" style="top:204px">
    <div class="office__block"><div class="office__label">HEADQUARTER:</div>84 Carrow Street, Kelmscott, WA 6111</div>
    <div class="office__block"><div class="office__label">LOCATION:</div>Australia | Singapore | Indonesia | Vietnam</div>
  </div>
  <div class="contact" style="top:202px">
    <div><span class="contact__key">T</span>| +614 00 555 218</div>
    <div><span class="contact__key">F</span>| +618 90005512</div>
    <div><span class="contact__key">W</span>| www.dravoline.com.au</div>
    <div class="contact__social"><span class="contact__dot"></span>@dravolineindustrial</div>
  </div>
  <div class="banner banner--sunset" style="top:256px;height:89px" role="img" aria-label="Refinery towers and a tanker ship at sunset"></div>
  <div class="products products--overlay products--gold" style="top:320px">
    <span>COMPOSITE HOSE</span><span>CONVOLUTED HOSE</span><span>METAL EXPANSION JOINTS</span><span>FABRIC EXPANSION JOINTS</span><span>RUBBER EXPANSION JOINTS</span>
  </div>
</section>

<!-- Option 2: dusk band, product line below -->
<section class="signature signature--dusk">
  <p class="sign-off" style="top:101px">Thanks and Regards
    <span class="sign-off__name">MARK HALLAM</span>
    <span class="sign-off__role">Managing Director</span>
  </p>
  <div class="brand" style="top:205px"><span class="brand__mark"></span><span class="brand__name">DRAVOLINE</span></div>
  <div class="office" style="top:204px">
    <div class="office__block"><div class="office__label">HEADQUARTER:</div>84 Carrow Street, Kelmscott, WA 6111</div>
    <div class="office__block"><div class="office__label">LOCATION:</div>Australia | Singapore | Indonesia | Vietnam</div>
  </div>
  <div class="contact" style="top:202px">
    <div><span class="contact__key">T</span>| +614 00 555 218</div>
    <div><span class="contact__key">F</span>| +618 90005512</div>
    <div><span class="contact__key">W</span>| www.dravoline.com.au</div>
    <div class="contact__social"><span class="contact__dot"></span>@dravolineindustrial</div>
  </div>
  <div class="banner banner--dusk" style="top:256px;height:89px" role="img" aria-label="Lit petrochemical refinery at dusk under a pink sky"></div>
  <div class="products products--plain" style="top:352px">
    <span>COMPOSITE HOSE</span><span>CONVOLUTED HOSE</span><span>METAL EXPANSION JOINTS</span><span>FABRIC EXPANSION JOINTS</span><span>RUBBER EXPANSION JOINTS</span>
  </div>
</section>

<!-- Option 3: night band, partner badges -->
<section class="signature signature--night">
  <p class="sign-off" style="top:66px">Thanks and Regards
    <span class="sign-off__name">MARK HALLAM</span>
    <span class="sign-off__role">Managing Director</span>
  </p>
  <div class="brand" style="top:170px"><span class="brand__mark"></span><span class="brand__name">DRAVOLINE</span></div>
  <div class="office" style="top:169px">
    <div class="office__block"><div class="office__label">HEADQUARTER:</div>84 Carrow Street, Kelmscott, WA 6111</div>
    <div class="office__block"><div class="office__label">LOCATION:</div>Australia | Singapore | Indonesia | Vietnam</div>
  </div>
  <div class="contact" style="top:167px">
    <div><span class="contact__key">T</span>| +614 00 555 218</div>
    <div><span class="contact__key">F</span>| +618 90005512</div>
    <div><span class="contact__key">W</span>| www.dravoline.com.au</div>
    <div class="contact__social"><span class="contact__dot"></span>@dravolineindustrial</div>
  </div>
  <div class="banner banner--night" style="top:222px;height:89px" role="img" aria-label="Brightly lit refinery at night"></div>
  <div class="products products--overlay products--light" style="top:286px">
    <span>COMPOSITE HOSE</span><span>CONVOLUTED HOSE</span><span>METAL EXPANSION JOINTS</span><span>FABRIC EXPANSION JOINTS</span><span>RUBBER EXPANSION JOINTS</span>
  </div>
  <div class="partners" aria-label="Partner and certification badges">
    <span class="partners__badge" style="width:76px"></span>
    <span class="partners__badge" style="width:44px"></span>
    <span class="partners__badge" style="width:22px"></span>
    <span class="partners__badge" style="width:22px"></span>
    <span class="partners__badge" style="width:26px"></span>
    <span class="partners__badge" style="width:32px;background:#2c3a6a"></span>
    <span class="partners__badge partners__badge--round"></span>
    <span class="partners__badge" style="width:56px"></span>
  </div>
</section>

</body>
</html>
```